Postcard Design

The business Logo is 'Brambo' it is grass cutting and maintenance. It will offer grass cutting with stripes including edging. Other services include decking/fencing maintenance, lawn treatment and patio/drive cleaning...... prices start from £10 to include front and rear lawns, Regular cuts or a one off tidy. private and commercial. Contracts welcome.
call 01642385106 or 07481926053 for a free quote.
one of the pics that i have sent is the logo (obviously it would need to be tidied up and neater) that is just rough. The other pic is one of pello cards templates but is the one that is the preferred out of all of them. If it could be similar to that with the logo on would be great.
a before (long scruffy grass) and after (neat Lawn) half and half of the postcard would be great.

Target Market(s)

Middle class home owners.

Industry/Entity Type

Business

Requirements
Must have
• The 'Brambo' logo
Nice to have
• we have a lot of junk mail posted in this area and a lot just gets put in the bin so could you make it eye catching.

```html
<!DOCTYPE html>
<html lang="en">
<head>
<meta charset="utf-8">
<title>Brambo Lawn Care Postcard</title>
<link rel="stylesheet" href="https://fonts.googleapis.com/css2?family=Libre+Baskerville:wght@400;700&family=Nunito:wght@900&display=swap">
<style>
  :root {
    --band-green: #2ad100;
    --band-green-light: #4ee81a;
    --rule-green: #14a000;
    --lawn-dark: #2f9a12;
    --lawn-mid: #4cc21e;
    --lawn-light: #6fd638;
    --ink: #0a0a0a;
    --white: #ffffff;
    --service-yellow: #f2f20a;
    --burst-edge: #2a1500;
    --burst-orange: #f47a00;
    --burst-yellow: #ffe600;
  }
  html, body {
    margin: 0;
    padding: 0;
    width: 1200px;
    height: 930px;
    overflow: hidden;
    background: var(--white);
  }
  .postcard {
    position: relative;
    width: 1200px;
    height: 930px;
    overflow: hidden;
    font-family: "Libre Baskerville", "Times New Roman", serif;
  }
  .top-band, .bottom-band {
    position: absolute;
    left: 0;
    width: 1200px;
    background: linear-gradient(180deg, var(--band-green-light), var(--band-green) 60%, var(--band-green-light));
  }
  .top-band { top: 0; height: 206px; }
  .bottom-band { top: 750px; height: 180px; }
  .rule {
    position: absolute;
    left: 0;
    width: 1200px;
    height: 6px;
    background: var(--rule-green);
  }
  .rule--top { top: 206px; }
  .rule--bottom { top: 744px; }
  .lawn-photo {
    position: absolute;
    top: 212px;
    left: 0;
    width: 1200px;
    height: 532px;
    background:
      repeating-linear-gradient(100deg, rgba(255,255,255,0.06) 0 110px, rgba(0,0,0,0.05) 110px 220px),
      radial-gradient(ellipse at 50% 30%, var(--lawn-light), var(--lawn-mid) 55%, var(--lawn-dark));
  }
  .headline {
    position: absolute;
    top: 78px;
    left: 0;
    width: 1200px;
    margin: 0;
    text-align: center;
    font-weight: 700;
    font-size: 48px;
    line-height: 60px;
    color: var(--ink);
    letter-spacing: 1px;
  }
  .brand-name {
    position: absolute;
    top: 290px;
    left: 268px;
    width: 740px;
    margin: 0;
    text-align: center;
    font-weight: 700;
    font-size: 132px;
    line-height: 220px;
    color: var(--white);
    letter-spacing: 2px;
    white-space: nowrap;
  }
  .brand-tagline {
    position: absolute;
    top: 548px;
    left: 0;
    width: 1200px;
    margin: 0;
    text-align: center;
    font-weight: 700;
    font-size: 92px;
    line-height: 100px;
    color: var(--white);
    letter-spacing: 14px;
    white-space: nowrap;
  }
  .services {
    position: absolute;
    top: 646px;
    left: 0;
    width: 1200px;
    margin: 0;
    padding: 0;
    list-style: none;
    text-align: center;
    font-size: 25px;
    line-height: 29px;
    color: var(--service-yellow);
    letter-spacing: 1px;
    text-shadow: 2px 2px 2px rgba(0,0,0,0.75);
  }
  .price-burst {
    position: absolute;
    top: 318px;
    left: 66px;
    width: 190px;
    height: 190px;
  }
  .price-burst__text {
    position: absolute;
    inset: 0;
    text-align: center;
    color: var(--ink);
    transform: rotate(-10deg);
  }
  .price-burst__label {
    display: block;
    margin-top: 46px;
    font-size: 15px;
    line-height: 17px;
    font-weight: 700;
  }
  .price-burst__amount {
    display: block;
    font-size: 62px;
    line-height: 70px;
    font-weight: 700;
  }
  .phone-line {
    position: absolute;
    top: 768px;
    left: 0;
    width: 1200px;
    margin: 0;
    text-align: center;
    font-family: "Nunito", "Arial Rounded MT Bold", sans-serif;
    font-weight: 900;
    font-size: 68px;
    line-height: 80px;
    color: var(--white);
    text-shadow: 4px 4px 0 #222, 5px 5px 3px rgba(0,0,0,0.6);
  }
  .phone-line__or {
    font-size: 30px;
    margin: 0 10px;
  }
  .call-to-action {
    position: absolute;
    top: 846px;
    left: 0;
    width: 1200px;
    margin: 0;
    text-align: center;
    font-size: 35px;
    line-height: 46px;
    color: var(--ink);
    letter-spacing: 1px;
  }
</style>
</head>
<body>
<main class="postcard">
  <div class="top-band"></div>
  <div class="lawn-photo" role="img" aria-label="Photograph of a freshly mown striped green lawn"></div>
  <div class="rule rule--top"></div>
  <div class="rule rule--bottom"></div>
  <div class="bottom-band"></div>

  <h2 class="headline">RELIABLE &amp; AFFORDABLE<br>COMMERCIAL &amp; RESIDENTIAL</h2>

  <h1 class="brand-name">BRAMBO</h1>
  <p class="brand-tagline">LAWN CARE</p>

  <ul class="services">
    <li>OTHER SERVICES OFFERED</li>
    <li>DECKING/FENCING MAINTENANCE</li>
    <li>LAWN TREATMENT AND PATIO/DRIVE CLEANING</li>
  </ul>

  <div class="price-burst">
    <svg width="190" height="190" viewBox="0 0 190 190" aria-hidden="true">
      <defs>
        <radialGradient id="burstFill" cx="50%" cy="45%" r="55%">
          <stop offset="0%" stop-color="#ffe600"/>
          <stop offset="60%" stop-color="#ffb000"/>
          <stop offset="100%" stop-color="#f47a00"/>
        </radialGradient>
      </defs>
      <g transform="translate(95 95)" fill="#2a1500">
        <rect x="-66" y="-66" width="132" height="132" transform="rotate(0)"/>
        <rect x="-66" y="-66" width="132" height="132" transform="rotate(7.5)"/>
        <rect x="-66" y="-66" width="132" height="132" transform="rotate(15)"/>
        <rect x="-66" y="-66" width="132" height="132" transform="rotate(22.5)"/>
        <rect x="-66" y="-66" width="132" height="132" transform="rotate(30)"/>
        <rect x="-66" y="-66" width="132" height="132" transform="rotate(37.5)"/>
        <rect x="-66" y="-66" width="132" height="132" transform="rotate(45)"/>
        <rect x="-66" y="-66" width="132" height="132" transform="rotate(52.5)"/>
        <rect x="-66" y="-66" width="132" height="132" transform="rotate(60)"/>
        <rect x="-66" y="-66" width="132" height="132" transform="rotate(67.5)"/>
        <rect x="-66" y="-66" width="132" height="132" transform="rotate(75)"/>
        <rect x="-66" y="-66" width="132" height="132" transform="rotate(82.5)"/>
        <circle r="82" fill="url(#burstFill)"/>
      </g>
    </svg>
    <div class="price-burst__text">
      <span class="price-burst__label">PRICES START<br>FROM</span>
      <span class="price-burst__amount">£10</span>
    </div>
  </div>

  <p class="phone-line">01642385106<span class="phone-line__or">OR</span>07481926053</p>
  <p class="call-to-action">CALL TODAY FOR FREE ESTIMATE</p>
</main>
</body>
</html>
```